Business Cards for Corvantis LLC

We need business cards for a new company called “Corvantis LLC”. This is a technology process improvement company providing a comprehensive assessment of the technology used to run their business. The documentation and review process delivers the visibility and reassurance they need to protect their business and plan for the future. The product is called “Halvorne Ledgerwork”. Our primary target is small-medium size businesses, with the deliverables going to the decision maker. We would like to see the designs use the color blue. Our tag line is PROTECT YOUR BUSINESS · TAKE CONTROL OF IT.

Industry/Entity Type

Business

Contact Information for Business Card

Tag line should be on back of card - it does not have to be upper case.

Requirements
Must have
• Please use information when laying out card:
• Name: Darnell Pruitt
• Title: Partner
• Phone Number: (877)555-0143
• Email: dell@corvantisllc.com
• Website: http://corvantisllc.com

```html
<!DOCTYPE html>
<html lang="en">
<head>
<meta charset="UTF-8">
<title>Corvantis LLC — Business Cards</title>
<link rel="stylesheet" href="https://fonts.googleapis.com/css2?family=Open+Sans:wght@400;600;700&display=swap">
<style>
  :root {
    --page-bg: #eceeef;
    --brand-blue: #1f7fc0;
    --brand-blue-light: #2d9ad6;
    --brand-blue-dark: #1565a6;
    --card-white: #f4f4f4;
    --card-white-edge: #e2e2e2;
    --text-grey: #6b6b6b;
    --text-dark: #4a4a4a;
    --rule-grey: #9a9a9a;
    --on-blue: #ffffff;
  }
  * { box-sizing: border-box; margin: 0; padding: 0; }
  html, body {
    width: 1200px;
    height: 900px;
    overflow: hidden;
    background: var(--page-bg);
    font-family: "Open Sans", Arial, sans-serif;
  }
  .sheet {
    width: 1200px;
    height: 900px;
    display: flex;
    flex-direction: column;
    align-items: center;
    justify-content: center;
    gap: 56px;
  }
  .card {
    width: 620px;
    height: 354px;
    border-radius: 3px;
    box-shadow: 0 10px 24px rgba(0,0,0,0.18);
    position: relative;
    overflow: hidden;
  }

  /* Front (blue) */
  .card--front {
    background: radial-gradient(ellipse at 55% 40%, var(--brand-blue-light) 0%, var(--brand-blue) 55%, var(--brand-blue-dark) 100%);
    display: flex;
    flex-direction: column;
    align-items: center;
    justify-content: center;
    color: var(--on-blue);
  }
  .wordmark {
    display: flex;
    align-items: center;
    gap: 14px;
    font-weight: 700;
    letter-spacing: 2px;
    text-transform: uppercase;
  }
  .wordmark__mark {
    width: 34px;
    height: 34px;
  }
  .card--front .wordmark { font-size: 38px; color: var(--on-blue); }
  .card--front .wordmark__mark { background: var(--on-blue); }
  .wordmark-rule {
    width: 260px;
    height: 3px;
    margin-top: 12px;
    background: linear-gradient(90deg, transparent, rgba(255,255,255,0.75) 20%, rgba(255,255,255,0.75) 80%, transparent);
  }
  .tagline {
    margin-top: 34px;
    font-size: 15px;
    font-weight: 400;
    letter-spacing: 0.4px;
    text-transform: uppercase;
  }

  /* Back (white) */
  .card--back {
    background: radial-gradient(ellipse at 60% 35%, #fbfbfb 0%, var(--card-white) 55%, var(--card-white-edge) 100%);
    display: flex;
    align-items: center;
    padding: 0 48px 0 52px;
  }
  .card--back .brand {
    flex: 1;
    display: flex;
    flex-direction: column;
    align-items: flex-start;
    margin-top: 60px;
  }
  .card--back .wordmark { font-size: 32px; color: var(--brand-blue); }
  .card--back .wordmark__mark { width: 28px; height: 28px; background: var(--brand-blue); }
  .card--back .wordmark-rule {
    width: 240px;
    background: linear-gradient(90deg, transparent, var(--rule-grey) 20%, var(--rule-grey) 80%, transparent);
  }
  .contact {
    width: 230px;
    margin-top: -40px;
  }
  .contact__name {
    font-size: 21px;
    color: var(--text-grey);
    font-weight: 400;
  }
  .contact__name strong { color: var(--text-dark); font-weight: 700; }
  .contact__title {
    font-size: 14px;
    color: var(--brand-blue);
    margin: 4px 0 18px 22px;
  }
  .contact__list { list-style: none; }
  .contact__item {
    display: flex;
    align-items: center;
    gap: 10px;
    font-size: 14px;
    color: var(--text-dark);
    margin-bottom: 9px;
  }
  .contact__icon { width: 16px; height: 16px; flex: none; fill: var(--brand-blue); }
</style>
</head>
<body>
  <main class="sheet">
    <section class="card card--front" aria-label="Business card front">
      <div class="wordmark">
        <span class="wordmark__mark" aria-hidden="true"></span>
        <span class="wordmark__name">Corvantis LLC</span>
      </div>
      <div class="wordmark-rule" aria-hidden="true"></div>
      <p class="tagline">Protect your business · Take control of IT.</p>
    </section>

    <section class="card card--back" aria-label="Business card back">
      <div class="brand">
        <div class="wordmark">
          <span class="wordmark__mark" aria-hidden="true"></span>
          <span class="wordmark__name">Corvantis LLC</span>
        </div>
        <div class="wordmark-rule" aria-hidden="true"></div>
      </div>
      <div class="contact">
        <p class="contact__name">Darnell <strong>Pruitt</strong></p>
        <p class="contact__title">Partner</p>
        <ul class="contact__list">
          <li class="contact__item">
            <svg class="contact__icon" viewBox="0 0 16 16" aria-hidden="true"><path d="M2 5c0-2 2-3 6-3s6 1 6 3v1h-3V5H5v1H2z M4 7h8l1 6H3z"/><circle cx="8" cy="10" r="1.6" fill="#fff"/></svg>
            <span>(877)555-0143</span>
          </li>
          <li class="contact__item">
            <svg class="contact__icon" viewBox="0 0 16 16" aria-hidden="true"><rect x="1" y="3" width="14" height="10" rx="1"/><path d="M1.5 3.5 8 9l6.5-5.5" fill="none" stroke="#fff" stroke-width="1.2"/></svg>
            <span>dell@corvantisllc.com</span>
          </li>
          <li class="contact__item">
            <svg class="contact__icon" viewBox="0 0 16 16" aria-hidden="true"><circle cx="8" cy="8" r="7"/><g fill="none" stroke="#fff" stroke-width="0.9"><ellipse cx="8" cy="8" rx="3" ry="7"/><path d="M1 8h14M2.5 4.5h11M2.5 11.5h11"/></g></svg>
            <span>corvantisllc.com</span>
          </li>
        </ul>
      </div>
    </section>
  </main>
</body>
</html>
```